Druckvorlage für Werbeanzeige einer Ferienwohnung gesucht.
Zielgruppe
Wir bieten ganzjährig eine große Ferienwohnung an ; d.h. für bis zu 7 Personen bei 4 Schlafzimmern, verteilt über zwei Ebenen, 2 Bäder, eine offene Wohnküche. Eine große Dachterrasse und ein kleiner Balkon mit Blick auf Ostsee und Binnensee runden das Ganze ab. Fußweg zur Ostsee 800m, an der Hohwachter Bucht gelegen,
Stellplatz am Haus, kleiner Schuppen für Fahrräder etc.
Angesprochen werden sollen Familien mit Kindern, große Familien
( eventuell generationsübergreifend), befreundete Menschen / Gruppen / Paare.
Aufgabenstellung
Einbindung des Logos,
im Text sollen auf jeden Fall die Kontaktdaten enthalten sein.
Mir wäre eine sehr freundliche Gestaltung wichtig, gerne mit kräftigen Farben, die u.a. das "Blau" der Ostsee wiedergeben ; gerne zwischendurch eine andere Schriftart.
Slogan kann, muss aber nicht ... z.B. "Ferien für GROß & klein" oder " Urlaub im Möwenhügel" oder ähnlich, wenn es denn passt !
Druckvorlage soll für eine Lokalzeittung sein und für Informationsbroschüren im ländlichen Bereich, z.B. bei der Feuerwehr, im Schützenverein etc ; Format einzeilig / 45mm.

```html
<!DOCTYPE html>
<html lang="de">
<head>
<meta charset="utf-8">
<title>Ferienwohnung an der Ostsee – Anzeige</title>
<link rel="stylesheet" href="https://fonts.googleapis.com/css2?family=Indie+Flower&family=Open+Sans:wght@400;700&display=swap">
<style>
  :root {
    --page-bg: #ecebe8;
    --sky-top: #4f93d8;
    --sky-bottom: #cfe6f6;
    --sea-deep: #3f6f9e;
    --sea-light: #b9d6ea;
    --meadow: #b9d45a;
    --sun: #f5a93a;
    --ink: #1d1d1d;
    --accent-red: #c0302a;
    --paper: #ffffff;
    --frame: #3a3a3a;
  }
  * { margin: 0; padding: 0; box-sizing: border-box; }
  html, body { width: 1200px; height: 775px; overflow: hidden; background: var(--page-bg); }
  .ad {
    position: absolute; left: 221px; top: 17px;
    width: 758px; height: 740px;
    background: var(--paper);
    border: 2px solid var(--frame);
    overflow: hidden;
  }
  .ad__sky {
    position: absolute; left: 0; top: 0; width: 100%; height: 340px;
    background: linear-gradient(to bottom, var(--sky-top), var(--sky-bottom));
  }
  .ad__sea {
    position: absolute; left: 0; top: 322px; width: 100%; height: 110px;
    background: linear-gradient(to bottom, var(--sea-deep), var(--sea-light) 60%, var(--paper));
  }
  .ad__headline {
    position: absolute; left: 30px; top: 18px;
    font-family: "Indie Flower", cursive;
    font-size: 100px; line-height: 140px;
    color: var(--ink); font-weight: 400;
  }
  .ad__headline span { display: block; }
  .ad__headline span + span { padding-left: 50px; }
  .ad__sun {
    position: absolute; left: 552px; top: 36px; width: 128px; height: 128px;
    border-radius: 50%;
    background: radial-gradient(circle, var(--sun) 55%, rgba(245,169,58,0) 72%);
  }
  .ad__kids {
    position: absolute; left: 172px; top: 318px; width: 412px; height: 140px;
    border-radius: 60px;
    background: linear-gradient(to bottom, rgba(185,212,90,0.35), var(--meadow));
  }
  .ad__contact {
    position: absolute; left: 41px; top: 494px;
    font-family: "Open Sans", sans-serif;
    font-size: 40px; line-height: 55px; color: var(--ink);
  }
  .ad__contact .label { display: inline-block; width: 168px; }
  .ad__web { color: var(--accent-red); font-weight: 700; }
</style>
</head>
<body>
  <div class="ad">
    <div class="ad__sky"></div>
    <div class="ad__sea"></div>
    <div class="ad__sun" role="img" aria-label="Gezeichnete lachende Sonne"></div>
    <h1 class="ad__headline"><span>Ferienwohnung</span><span>an der Ostsee</span></h1>
    <div class="ad__kids" role="img" aria-label="Drei gezeichnete Kinder am Strand auf grüner Wiese"></div>
    <div class="ad__contact">
      <p>Dünenweg 7 · 24399 Strandhof</p>
      <p><span class="label">Telefon:</span>04210 - 48 26 19</p>
      <p><span class="label">Mobil:</span>0152 - 634 71 985</p>
      <p class="ad__web">www.moewenhuegel-strandhof.de</p>
    </div>
  </div>
</body>
</html>
```